Logo and Card design for KRV Home Solutions LLC

I need an edgier logo and business card designs. Current logo attached. I like the colors below. I would like the logo to incorporate a home in the design.
Title = Principal-Acquisitions
Email:KRVHOMESOLUTIONS@mailnest.example
555-014-2739
facebook
IG
2 sided business card with the front being contact info a slogan about selling a home fast. The back incorporating What we do. Buy houses, land, or commercial property as is. We find solutions to make the process of selling simple and fair.

Target Market(s)

Motivated house sellers.

Industry/Entity Type

Business

Contact Information for Business Card

Who we are: We are a Faith based Real Estate Investment Company. We pay cash for homes in any condition and can close quick. Whatever the reason you need to sell fast, we can help. We believe in creating win-win solutions to help you in your time of need. We care! We can help!

Logo Text

KRV Home Solutions LLC

Font styles to use
Sans Serif

Colors
33a6d7
0355a3
85abd2
cee9f5
9d9d9d
b2b2b2
ffffff

Requirements
Must have
• Old logo attached. I want something edgier.
• Company name, phone number, description on the back of what we can do. Pay all cash. Buy in as is condition. No fees,Commisions or closing costs.Close quick. No hassles with solutions to meet your unique situation.
• Call today for an offer within 24 hours.

```html
<!DOCTYPE html>
<html lang="en">
<head>
<meta charset="utf-8">
<title>KRV Home Solutions – Business Card</title>
<link href="https://fonts.googleapis.com/css2?family=Montserrat:wght@500;600;700&family=Work+Sans:wght@400;500&display=swap" rel="stylesheet">
<style>
  :root {
    --navy: #213a76;
    --white: #ffffff;
    --ink-grey: #4a4a4a;
    --soft-grey: #9d9d9d;
    --band-grey: #5c5f66;
    --panel: #f6f7f9;
    --backdrop: #d9dadc;
  }
  * { margin: 0; padding: 0; box-sizing: border-box; }
  html, body { width: 1200px; height: 900px; overflow: hidden; }
  body {
    background: var(--backdrop);
    position: relative;
    font-family: "Work Sans", sans-serif;
  }
  .card {
    position: absolute;
    width: 700px;
    height: 400px;
    left: 250px;
    box-shadow: 0 10px 24px rgba(0,0,0,0.22);
    overflow: hidden;
  }
  /* Back side */
  .card-back {
    top: 30px;
    background: var(--navy);
    color: var(--white);
    text-align: center;
  }
  .brand-mark {
    margin-top: 96px;
    display: inline-flex;
    align-items: center;
    gap: 14px;
  }
  .brand-mark .dot {
    width: 18px; height: 18px;
    border-radius: 50%;
    background: var(--white);
  }
  .brand-mark .name {
    font-family: "Montserrat", sans-serif;
    font-weight: 700;
    font-size: 34px;
    letter-spacing: 1px;
    color: var(--white);
  }
  .services {
    margin: 60px auto 0;
    width: 520px;
    font-size: 16px;
    line-height: 1.45;
    letter-spacing: 0.5px;
  }
  /* Front side */
  .card-front {
    top: 470px;
    background: var(--white);
  }
  .front-panel {
    position: absolute;
    right: 0; top: 0;
    width: 360px; height: 400px;
    background: linear-gradient(160deg, var(--white) 20%, var(--panel) 70%);
  }
  .company {
    position: absolute;
    left: 50px; top: 158px;
    font-family: "Montserrat", sans-serif;
    font-weight: 600;
    font-size: 30px;
    line-height: 36px;
    color: var(--navy);
    letter-spacing: 0.5px;
  }
  .role {
    position: absolute;
    left: 46px; top: 198px;
    font-size: 17px;
    line-height: 22px;
    color: var(--ink-grey);
    letter-spacing: 0.5px;
  }
  .rule {
    position: absolute;
    left: 46px; right: 30px; top: 230px;
    height: 2px;
    background: var(--navy);
  }
  .contacts {
    position: absolute;
    left: 46px; top: 244px;
    list-style: none;
  }
  .contacts li {
    display: flex;
    align-items: center;
    gap: 12px;
    font-size: 16px;
    color: var(--ink-grey);
    letter-spacing: 0.6px;
    height: 23px;
    white-space: nowrap;
  }
  .contacts .icon {
    width: 16px; height: 16px;
    flex: none;
  }
  .contacts .tile {
    width: 14px; height: 14px;
    border-radius: 3px;
    background: var(--navy);
    flex: none;
    margin: 0 1px;
  }
  .slogan {
    position: absolute;
    right: 40px; bottom: 30px;
    font-family: "Montserrat", sans-serif;
    font-weight: 500;
    font-size: 17px;
    line-height: 20px;
    letter-spacing: 3px;
    color: var(--ink-grey);
    white-space: nowrap;
  }
  .footer-bands {
    position: absolute;
    left: 0; bottom: 0;
    width: 700px; height: 18px;
  }
</style>
</head>
<body>

  <section class="card card-back" aria-label="Card back">
    <div class="brand-mark">
      <span class="dot"></span>
      <span class="name">KRV HOME SOLUTIONS</span>
    </div>
    <p class="services">
      Pay all cash. Buy in as is condition. No fees,Commisions
      or closing costs.Close quick. No hassles with solutions
      to meet your unique situation.<br>
      Call today for an offer within 24 hours.
    </p>
  </section>

  <section class="card card-front" aria-label="Card front">
    <div class="front-panel"></div>
    <h1 class="company">KRV HOME SOLUTIONS</h1>
    <p class="role">Principal-Acquisitions</p>
    <div class="rule"></div>
    <ul class="contacts">
      <li>
        <svg class="icon" viewBox="0 0 16 16" aria-hidden="true">
          <circle cx="8" cy="8" r="8" fill="#213a76"/>
          <path d="M5.2 4.2l1.6-.4.9 2-1 .8c.5 1 1.2 1.7 2.2 2.2l.8-1 2 .9-.4 1.6c-3.4.2-6.3-2.7-6.1-6.1z" fill="#fff"/>
        </svg>
        555-014-2739
      </li>
      <li><span class="tile"></span>/krvhomesolutions</li>
      <li><span class="tile"></span>@krvhomesolutions</li>
      <li>
        <svg class="icon" viewBox="0 0 16 16" aria-hidden="true">
          <circle cx="8" cy="8" r="8" fill="#213a76"/>
          <rect x="4" y="5" width="8" height="6" rx="1" fill="none" stroke="#fff" stroke-width="1.2"/>
          <path d="M4.3 5.4L8 8.3l3.7-2.9" fill="none" stroke="#fff" stroke-width="1.2"/>
        </svg>
        krvhomesolutions@mailnest.example
      </li>
    </ul>
    <p class="slogan">SELLING A HOME FAST</p>
    <svg class="footer-bands" viewBox="0 0 700 18" preserveAspectRatio="none" aria-hidden="true">
      <polygon points="0,0 340,6 325,18 0,18" fill="#213a76"/>
      <polygon points="350,6 700,12 700,18 335,18" fill="#5c5f66"/>
    </svg>
  </section>

</body>
</html>
```